Darrow Consulting needs a quality & professional business card!

I am a recruitment and employment consultant from Brisbane, Australia and I had a fantastic logo organised by this community to I am hoping the business card will be the same.

I have attached the Darrow consulting logo that ideally would feature on the back of the business card. There are a number of logos for you to use as you see fit. I would like the colour cheme to match that of the Darrow Consulting logo. I also have a secondary company called Career Lantern Australia and I have included that logo as well. While it is an important part of the business I don't want this logo feature too predominantly as I am moving out of this space. This logo was created by myself and is of low quality. Feel free to use the icon and words however you want. The winning design will be smart, professional and eye-catching.

The information I am looking for in the business card is:
Name: Gavin Darrow
Position: Founder & Director
Phone: (07) 3519 6482
Mobile: 0431 586 207
Email: gavin@careerlantern.com.au

Target Market(s)

Recruiters, government, large companies

Contact Information for Business Card

Name: Gavin Darrow
Phone: (07) 3519 6482
Mobile: 0431 586 207
Web: www.careerlantern.com.au

Font styles to use
Serif
Sans Serif

Requirements
Must have
• Darrow Consulting Logo on reverse side
• Contact details on front side with smaller reference to Darrow Consulting logo and Career Lantern Australia logo

```html
<!DOCTYPE html>
<html lang="en">
<head>
<meta charset="utf-8">
<title>Darrow Consulting – Business Card</title>
<link rel="stylesheet" href="https://fonts.googleapis.com/css2?family=Michroma&family=Exo+2:wght@600;700&display=swap">
<style>
  :root {
    --backdrop: #3a3b3d;
    --card: #25272a;
    --band: #e08530;
    --text-light: #f1f1f1;
    --text-muted: #bfc0c2;
    --accent: #e08530;
  }
  * { box-sizing: border-box; margin: 0; padding: 0; }
  html, body { width: 1200px; height: 1000px; overflow: hidden; }
  body {
    background: var(--backdrop);
    position: relative;
    font-family: "Michroma", sans-serif;
  }
  .card {
    position: absolute;
    left: 220px;
    width: 760px;
    height: 434px;
    background: var(--card);
    border-radius: 26px;
    overflow: hidden;
  }
  .card--back { top: 50px; }
  .card--front { top: 516px; }

  .wordmark {
    position: absolute;
    display: flex;
    align-items: center;
    gap: 22px;
    color: var(--text-light);
    font-family: "Michroma", sans-serif;
    font-weight: 400;
  }
  .wordmark__square {
    width: 70px; height: 70px;
    background: var(--text-muted);
    flex: none;
  }
  .wordmark__name { line-height: 1.15; letter-spacing: 0.04em; }
  .card--back .wordmark { left: 170px; top: 158px; font-size: 40px; }
  .card--back .wordmark__square { width: 96px; height: 96px; }
  .card--front .wordmark { right: 60px; top: 210px; font-size: 28px; }

  .band {
    position: absolute;
    left: 0; top: 60px;
    width: 100%; height: 78px;
    background: var(--band);
    padding: 12px 0 0 50px;
    color: #fff;
    font-family: "Exo 2", sans-serif;
  }
  .band__name { font-size: 28px; font-weight: 700; letter-spacing: 0.02em; line-height: 1.1; }
  .band__role { font-size: 18px; font-weight: 600; letter-spacing: 0.03em; }

  .partner {
    position: absolute;
    left: 40px; bottom: 54px;
    display: flex; align-items: center; gap: 8px;
    color: var(--text-muted);
    font-family: "Exo 2", sans-serif;
    font-weight: 600;
    font-size: 15px;
  }
  .partner__circle {
    width: 22px; height: 22px;
    border: 3px solid var(--text-muted);
    border-radius: 50%;
  }

  .contact {
    position: absolute;
    right: 46px; bottom: 34px;
    list-style: none;
    text-align: right;
    color: var(--text-light);
    font-size: 15px;
    line-height: 26px;
  }
  .contact li { display: flex; justify-content: flex-end; align-items: center; gap: 12px; }
  .contact svg { width: 16px; height: 16px; flex: none; }
</style>
</head>
<body>

  <section class="card card--back" aria-label="Card back">
    <div class="wordmark">
      <span class="wordmark__square"></span>
      <span class="wordmark__name">DARROW<br>CONSULTING</span>
    </div>
  </section>

  <section class="card card--front" aria-label="Card front">
    <div class="band">
      <div class="band__name">GAVIN DARROW</div>
      <div class="band__role">Founder &amp; Director</div>
    </div>

    <div class="wordmark">
      <span class="wordmark__square"></span>
      <span class="wordmark__name">DARROW<br>CONSULTING</span>
    </div>

    <div class="partner">
      <span class="partner__circle"></span>
      <span>Career Lantern Australia</span>
    </div>

    <ul class="contact">
      <li>(07) 3519 6482
        <svg viewBox="0 0 16 16" aria-hidden="true"><path d="M3 2l3 0 1 4-2 1c1 2 2 3 4 4l1-2 4 1 0 3c0 1-1 2-2 2C7 15 1 9 1 4c0-1 1-2 2-2z" fill="var(--accent)"/></svg>
      </li>
      <li>0431 586 207
        <svg viewBox="0 0 16 16" aria-hidden="true"><rect x="4" y="1" width="8" height="14" rx="1.5" fill="none" stroke="var(--accent)" stroke-width="1.6"/><circle cx="8" cy="12.5" r="0.9" fill="var(--accent)"/></svg>
      </li>
      <li>gavin@careerlantern.com.au
        <svg viewBox="0 0 16 16" aria-hidden="true"><rect x="1" y="3" width="14" height="10" rx="1" fill="var(--accent)"/><path d="M1.5 3.5L8 9l6.5-5.5" fill="none" stroke="var(--card)" stroke-width="1.4"/></svg>
      </li>
      <li>www.careerlantern.com.au
        <svg viewBox="0 0 16 16" aria-hidden="true"><circle cx="8" cy="8" r="7" fill="var(--accent)"/><path d="M1 8h14M8 1c-3 4-3 10 0 14M8 1c3 4 3 10 0 14" fill="none" stroke="var(--card)" stroke-width="1"/></svg>
      </li>
    </ul>
  </section>

</body>
</html>
```